Business Card Design Project

Business card design with a funky, clean, modern design. Business is an immigration consultancy. Client base will be Canadian employers wanting to hire or retain foreign workers and foreign nationals wanting to immigrate to Canada.

Full color possible, but should incorporate red/white/black as per the logo to be provided. Double sided card design.

Target Market(s)

Canadian employers looking to hire/retain staff and also foreign nationals immigrating to Canada

Industry/Entity Type

Business

Requirements
Must have
• Logo (to be provided)
Name (Marla Voskuil, Immigration Consultant)
Phone (604) 731-5562
E-mail: marla@tallowbrookmigration.example
Web: www.tallowbrookmigration.example

Nice to have
• Tag Line
Clean, modern style

```html
<!DOCTYPE html>
<html lang="en">
<head>
<meta charset="utf-8">
<title>Tallowbrook Migration – Business Card</title>
<link rel="stylesheet" href="https://fonts.googleapis.com/css2?family=Barlow:wght@400;500;700&display=swap">
<style>
  :root {
    --backdrop: #b5f3fd;
    --card-white: #ffffff;
    --brand-red: #ff1119;
    --accent-red: #e0141c;
    --ink: #16161a;
    --card-edge: #2a2a2a;
    --shadow: rgba(0, 0, 0, 0.5);
  }
  * { box-sizing: border-box; margin: 0; padding: 0; }
  html, body {
    width: 846px;
    height: 1200px;
    overflow: hidden;
    background: var(--backdrop);
    font-family: "Barlow", Arial, sans-serif;
  }
  .canvas {
    position: relative;
    width: 846px;
    height: 1200px;
  }
  .card {
    position: absolute;
    left: 140px;
    width: 575px;
    border: 1px solid var(--card-edge);
    box-shadow: -10px 8px 6px var(--shadow);
  }
  /* Front */
  .card--front {
    top: 113px;
    height: 378px;
    background: var(--card-white);
  }
  .office-list {
    position: absolute;
    top: 18px;
    left: 22px;
    right: 16px;
    display: flex;
    justify-content: space-between;
    list-style: none;
    color: var(--accent-red);
    font-size: 23px;
    font-weight: 500;
    letter-spacing: 0.3px;
  }
  .brand {
    position: absolute;
    left: 0;
    right: 0;
    top: 95px;
    display: flex;
    flex-direction: column;
    align-items: center;
  }
  .brand__mark {
    width: 96px;
    height: 96px;
    border-radius: 50%;
    background: var(--accent-red);
  }
  .brand__name {
    margin-top: 30px;
    color: var(--ink);
    font-size: 34px;
    font-weight: 700;
    letter-spacing: 1px;
    text-transform: uppercase;
    line-height: 1;
  }
  /* Back */
  .card--back {
    top: 679px;
    height: 364px;
    background: var(--brand-red);
    color: var(--card-white);
    font-weight: 500;
  }
  .tagline {
    position: absolute;
    top: 20px;
    left: 24px;
    font-size: 21px;
    line-height: 29px;
    letter-spacing: 0.3px;
  }
  .consultant {
    position: absolute;
    top: 168px;
    left: 0;
    right: 0;
    text-align: center;
    font-size: 21px;
    letter-spacing: 0.4px;
  }
  .contact {
    position: absolute;
    top: 256px;
    left: 24px;
    list-style: none;
    font-size: 21px;
    line-height: 29px;
    letter-spacing: 0.3px;
  }
</style>
</head>
<body>
<main class="canvas">
  <section class="card card--front" aria-label="Card front">
    <ul class="office-list">
      <li>Maple Ridge</li>
      <li>Burnaby</li>
      <li>Vancouver</li>
    </ul>
    <div class="brand">
      <span class="brand__mark" aria-hidden="true"></span>
      <span class="brand__name">Tallowbrook Migration</span>
    </div>
  </section>

  <section class="card card--back" aria-label="Card back">
    <p class="tagline">
      Infinite opportunity.<br>
      Infinite possibilities.<br>
      Infinte potential.
    </p>
    <p class="consultant">Marla Voskuil, RCIC</p>
    <ul class="contact">
      <li>(604) 731-5562</li>
      <li>marla@tallowbrookmigration.example</li>
      <li>www.tallowbrookmigration.example</li>
    </ul>
  </section>
</main>
</body>
</html>
```